Brackenfold Health Web Page

We need a visually exciting webpage that introduces people to our practice. We are a practice that has both physiotherapy and psychology and we need the page to reflect this. We are also split across two practice locations. We need the page to be able to be updated regularly to include a blog spot and the linking in of our facebook page. There should be tabs to introduce our practitioners with some blurbs about them, a tab for people to be able to contact us, a tab to read about physiotherapy services and a tab to talk about psychology services. If there are other tabs than please include these. We are a practice that has treated world class athlete on a regular basis and see our selves as leaders in the field and the website must reflect this. I do not want basic clip-arty type things that anyone could have, we have to have something that draws people in.
Firstly, thanks everyone for their designs. I have attached some links to some physiotherapy websites that I think contain some interesting information and/or layout, as well as some comments,
Hi all,
Reason: Hi Guys,
We are so very close to finding a great design. I feel that we just need a bit of extra time to be able to clinch where we want to be. Thanks for your fantastic designs :)
Regards,
Oliver and Ruth
- 2 Practice Addresses (details to follow for right applications)
Psychology aspect
Physiotherapy aspect
Ability to update blog

```html
<!DOCTYPE html>
<html lang="en">
<head>
<meta charset="utf-8">
<title>Brackenfold Health</title>
<link rel="stylesheet" href="https://fonts.googleapis.com/css2?family=Josefin+Sans:wght@600;700&family=Open+Sans:wght@400;600;700;800&display=swap">
<style>
:root{
  --purple:#6a3d9a;
  --green:#7cab3b;
  --teal:#1bb3c9;
  --ink:#222;
  --body:#666;
  --line:#e2e2e2;
  --pale:#f3f3f3;
  --dark:#171a17;
  --white:#fff;
}
*{box-sizing:border-box;margin:0;padding:0}
html,body{width:1200px;height:3243px;overflow:hidden}
body{font-family:"Open Sans",sans-serif;color:var(--body);background:var(--white);font-size:14px;line-height:1.6}
.wrap{width:920px;margin:0 auto;position:relative}
h2.section-title{font-family:"Josefin Sans",sans-serif;font-weight:700;color:var(--ink);font-size:30px;text-align:center;letter-spacing:1px;padding-top:12px}
h2.section-title::after{content:"";display:block;width:40px;height:4px;background:var(--purple);margin:10px auto 0}
h3.block-title{font-family:"Josefin Sans",sans-serif;font-weight:700;color:var(--ink);font-size:27px;letter-spacing:1px;white-space:nowrap}

/* header */
.site-header{height:108px;background:#f7f7f2}
.site-header .wrap{height:108px;display:flex;justify-content:space-between;align-items:center}
.brand{font-weight:800;color:var(--purple);font-size:30px;line-height:1;letter-spacing:-.5px;width:180px}
.call{display:flex;align-items:center;gap:10px;color:var(--ink)}
.call strong{display:block;font-size:23px;font-weight:600;line-height:1.1;white-space:nowrap}
.call small{display:block;font-size:13px;color:var(--body);text-align:right}

/* nav */
.main-nav{height:44px;background:var(--white);border-bottom:1px solid var(--line)}
.main-nav ul{list-style:none;display:flex;height:44px}
.main-nav a{display:block;height:44px;line-height:44px;padding:0 21px;font-size:12px;font-weight:700;color:var(--ink);text-decoration:none;text-transform:uppercase;white-space:nowrap}
.main-nav a.active{background:var(--purple);color:var(--white)}

/* hero */
.hero{height:496px;position:relative;background:linear-gradient(160deg,#a9c866 0%,#6f9c3a 45%,#4c7a2c 100%);overflow:hidden}
.hero-photo{position:absolute;left:140px;top:0;width:560px;height:496px;background:linear-gradient(180deg,rgba(255,255,255,.15),rgba(60,90,30,.25))}
.hero-inset{position:absolute;left:730px;top:100px;width:180px;height:180px;border-radius:50%;border:6px solid rgba(255,255,255,.8);background:linear-gradient(150deg,#c8d9a4,#8fb063)}
.hero h1{position:absolute;left:400px;top:14px;width:640px;color:var(--white);font-family:"Josefin Sans",sans-serif;font-weight:700;font-size:32px;line-height:1.15;text-transform:uppercase;letter-spacing:.5px}
.btn{display:inline-block;background:var(--teal);color:var(--white);font-weight:700;text-transform:uppercase;text-decoration:none;white-space:nowrap}
.hero .btn{position:absolute;left:865px;top:378px;width:195px;height:50px;line-height:50px;text-align:center;font-size:14px}
.slide-arrow{position:absolute;top:380px;width:36px;height:36px;border-radius:50%;background:rgba(255,255,255,.35);display:flex;align-items:center;justify-content:center}
.slide-arrow.prev{left:18px}.slide-arrow.next{right:18px}

/* about */
.about{height:502px;background:var(--pale)}
.about .wrap{display:flex;height:502px}
.about-text{width:440px;padding-top:40px}
.about-text p{font-size:13px;line-height:1.65;margin-top:16px}
.about-photo{margin-left:auto;width:460px;height:502px;background:linear-gradient(180deg,#e8e3dc,#cfd7d8)}

/* practitioners */
.practitioners{height:430px;padding-top:40px}
.team{display:flex;justify-content:space-between;margin-top:30px}
.member{width:142px}
.member .photo{height:101px;background:linear-gradient(135deg,#d9b98d,#9f7a55)}
.member:nth-child(2n) .photo{background:linear-gradient(135deg,#c9c7d6,#8d8aa3)}
.member h4{font-size:13px;font-weight:700;color:var(--ink);margin-top:10px}
.member p{font-size:12px;line-height:1.5;margin-top:2px}
.member .more{display:inline-block;margin-top:10px;background:var(--teal);color:var(--white);font-size:10px;font-weight:700;padding:2px 12px;border-radius:10px;text-decoration:none;white-space:nowrap}

/* news + booking */
.split{height:542px;background:var(--pale);border-top:1px solid var(--line);padding-top:40px}
.split .wrap{display:flex;justify-content:space-between}
.news{width:440px}
.tabs{display:flex;margin-top:14px;border-bottom:1px solid var(--line)}
.tabs span{padding:6px 16px;font-size:15px;color:#999}
.tabs span.on{background:var(--ink);color:var(--white)}
.post{display:flex;gap:16px;padding:18px 0;border-bottom:1px solid var(--line)}
.post .thumb{width:60px;height:60px;flex:none;background:linear-gradient(135deg,#e7c6b8,#b8554e)}
.post h5{font-size:13px;font-weight:700;color:var(--ink)}
.post p{font-size:12px;line-height:1.55}
.post a{color:var(--teal);text-decoration:none}
.booking{width:440px}
.booking form{margin-top:14px}
.field{display:block;width:440px;height:46px;background:var(--white);border:1px solid var(--line);margin-bottom:12px;padding:0 12px;line-height:44px;font-size:13px;color:#888}
.field.msg{height:140px}
.booking .btn{width:96px;height:50px;line-height:50px;text-align:center;font-size:14px;margin-top:4px}

/* services */
.services{height:270px;padding-top:40px}
.service-row{display:flex;justify-content:space-between;margin-top:30px}
.service{width:297px;height:122px}
.s1{background:linear-gradient(160deg,#f5c36a,#c97a2c)}
.s2{background:linear-gradient(160deg,#c9dbe6,#3b6fa5)}
.s3{background:linear-gradient(160deg,#f2efed,#b8b0aa)}

/* contact */
.contact{height:446px;padding-top:40px;border-top:1px solid var(--line)}
.locations{display:flex;justify-content:space-between;margin-top:30px}
.location{width:440px}
.map{height:156px;background:linear-gradient(135deg,#ece9e1,#dcd8cd)}
.location h4{font-size:17px;font-weight:700;color:var(--ink);margin:16px 0 8px}
.location li{list-style:none;display:flex;align-items:center;gap:10px;font-size:13px;margin-bottom:6px}
.location li a{color:var(--teal);text-decoration:none}

/* footer */
.site-footer{height:391px;background:var(--dark);position:relative;border-top:8px solid var(--teal)}
.site-footer .notch{position:absolute;left:578px;top:-1px}
.footer-cols{display:flex;padding-top:60px}
.footer-col h4{color:var(--green);font-size:15px;font-weight:700;margin-bottom:8px;white-space:nowrap}
.footer-col ul{list-style:none;columns:2;column-gap:20px}
.footer-col li{color:#ddd;font-size:13px;line-height:1.9;white-space:nowrap}
.col-physio{width:430px}.col-physio ul{width:410px}
.col-psych{width:210px}.col-psych ul{columns:1}
.social-box{width:280px;height:220px;background:var(--white);margin-left:auto;padding:10px;font-size:11px;color:var(--ink)}
.social-box strong{color:#3b5998;display:block;font-size:12px}
.faces{display:grid;grid-template-columns:repeat(6,1fr);gap:6px;margin-top:12px}
.faces span{height:36px;background:#cfd3da}
.social{position:absolute;left:140px;top:290px;display:flex;align-items:center;gap:8px;color:var(--green);font-weight:700;font-size:15px}
.social i{width:26px;height:26px;border-radius:50%;background:#555;display:block}
.social b{margin-right:8px;white-space:nowrap}
.footer-bottom{position:absolute;left:0;right:0;bottom:0;height:53px;background:#0c0d0c}
.footer-bottom .wrap{display:flex;justify-content:space-between;line-height:53px;font-size:12px;color:#ccc}
.footer-bottom nav span{margin-left:14px}
</style>
</head>
<body>

<header class="site-header">
  <div class="wrap">
    <div class="brand">Brackenfold Health</div>
    <div class="call">
      <svg width="26" height="30" viewBox="0 0 24 24"><path fill="#222" d="M6.6 10.8a15 15 0 0 0 6.6 6.6l2.2-2.2c.3-.3.7-.4 1-.2 1.1.4 2.3.6 3.6.6.6 0 1 .4 1 1V20c0 .6-.4 1-1 1A17 17 0 0 1 3 4c0-.6.4-1 1-1h3.5c.6 0 1 .4 1 1 0 1.3.2 2.5.6 3.6.1.3 0 .7-.2 1z"/></svg>
      <div><strong>Call Now 011 4820 7316</strong><small>Appointments 6am - 10pm 7 Days</small></div>
    </div>
  </div>
</header>

<nav class="main-nav">
  <div class="wrap">
    <ul>
      <li><a class="active" href="#">Home</a></li>
      <li><a href="#">About Us</a></li>
      <li><a href="#">Physiotherapy</a></li>
      <li><a href="#">Psychology</a></li>
      <li><a href="#">Our Practitioners</a></li>
      <li><a href="#">Group Classes</a></li>
      <li><a href="#">Contact Us</a></li>
    </ul>
  </div>
</nav>

<section class="hero">
  <div class="hero-photo" role="img" aria-label="Physiotherapist guiding a patient through a leg stretch on a treatment bench outdoors"></div>
  <div class="hero-inset" role="img" aria-label="Circular inset of a stretching session"></div>
  <h1>Lorem ipsum dolor sit amet,<br>consectetur</h1>
  <a class="btn" href="#">Find our more</a>
  <span class="slide-arrow prev"><svg width="12" height="14" viewBox="0 0 12 14"><path d="M9 1 3 7l6 6" fill="none" stroke="#fff" stroke-width="2.5"/></svg></span>
  <span class="slide-arrow next"><svg width="12" height="14" viewBox="0 0 12 14"><path d="m3 1 6 6-6 6" fill="none" stroke="#fff" stroke-width="2.5"/></svg></span>
</section>

<section class="about">
  <div class="wrap">
    <div class="about-text">
      <h3 class="block-title">ABOUT BRACKENFOLD HEALTH</h3>
      <p>Lorem ipsum dolor sit amet, consectetur adipisicing elit, sed do eiusmod tempor incididunt ut labore et dolore magna aliqua. Ut enim ad minim veniam, quis nostrud exercitation ullamco laboris nisi ut aliquip ex ea commodo consequat. Duis aute irure dolor in reprehenderit in voluptate velit esse cillum dolore eu fugiat nulla pariatur. Excepteur sint occaecat cupidatat non proident, sunt in culpa qui officia deserunt mollit anim id est laborum.</p>
      <p>Sed ut perspiciatis unde omnis iste natus error sit voluptatem accusantium doloremque laudantium, totam rem aperiam, eaque ipsa quae ab illo inventore veritatis et quasi architecto beatae vitae dicta sunt explicabo. Nemo enim ipsam voluptatem quia voluptas sit aspernatur aut odit aut fugit, sed quia consequuntur magni dolores eos qui ratione voluptatem sequi nesciunt.</p>
    </div>
    <div class="about-photo" role="img" aria-label="Practitioner in a teal polo shirt standing in the gym"></div>
  </div>
</section>

<section class="practitioners">
  <div class="wrap">
    <h2 class="section-title">OUR PRACTITIONERS</h2>
    <div class="team">
      <div class="member"><div class="photo" role="img" aria-label="Practitioner at work in the gym"></div><h4>Lorem Ipsum</h4><p>Lorem Ipsum is simply dummy text of the Sed ut perspicia tis unde omnis iste natus error sit</p><a class="more" href="#">read more &#9656;</a></div>
      <div class="member"><div class="photo" role="img" aria-label="Practitioner with a client"></div><h4>Lorem Ipsum</h4><p>Lorem Ipsum is simply dummy text of the Sed ut perspicia tis unde omnis iste natus error sit</p><a class="more" href="#">read more &#9656;</a></div>
      <div class="member"><div class="photo" role="img" aria-label="Practitioner treating a patient"></div><h4>Lorem Ipsum</h4><p>Lorem Ipsum is simply dummy text of the Sed ut perspicia tis unde omnis iste natus error sit</p><a class="more" href="#">read more &#9656;</a></div>
      <div class="member"><div class="photo" role="img" aria-label="Practitioner supervising exercise"></div><h4>Lorem Ipsum</h4><p>Lorem Ipsum is simply dummy text of the Sed ut perspicia tis unde omnis iste natus error sit</p><a class="more" href="#">read more &#9656;</a></div>
      <div class="member"><div class="photo" role="img" aria-label="Practitioner giving a massage"></div><h4>Lorem Ipsum</h4><p>Lorem Ipsum is simply dummy text of the Sed ut perspicia tis unde omnis iste natus error sit</p><a class="more" href="#">read more &#9656;</a></div>
      <div class="member"><div class="photo" role="img" aria-label="Practitioner in consultation"></div><h4>Lorem Ipsum</h4><p>Lorem Ipsum is simply dummy text of the Sed ut perspicia tis unde omnis iste natus error sit</p><a class="more" href="#">read more &#9656;</a></div>
    </div>
  </div>
</section>

<section class="split">
  <div class="wrap">
    <div class="news">
      <h3 class="block-title">LATEST NEWS</h3>
      <div class="tabs"><span class="on">Physiotherapy</span><span>Psychology</span></div>
      <article class="post"><div class="thumb" role="img" aria-label="Shoulder treatment"></div><div><h5>Lorem ipsum dolor sit amet, consectetur elit</h5><p>Sed ut perspiciatis unde omnis iste natus error sit voluptatem accusantium doloremque laudantium, totam rem aperiam, <a href="#">Read more</a></p></div></article>
      <article class="post"><div class="thumb" role="img" aria-label="Shoulder treatment"></div><div><h5>Lorem ipsum dolor sit amet, consectetur elit</h5><p>Sed ut perspiciatis unde omnis iste natus error sit voluptatem accusantium doloremque laudantium, totam rem aperiam, <a href="#">Read more</a></p></div></article>
      <article class="post"><div class="thumb" role="img" aria-label="Shoulder treatment"></div><div><h5>Lorem ipsum dolor sit amet, consectetur elit</h5><p>Sed ut perspiciatis unde omnis iste natus error sit voluptatem accusantium doloremque laudantium, totam rem aperiam, <a href="#">Read more</a></p></div></article>
    </div>
    <div class="booking">
      <h3 class="block-title">BOOK AN APPOINTMENT</h3>
      <form>
        <span class="field">Name</span>
        <span class="field">Email Address</span>
        <span class="field">Subject</span>
        <span class="field msg">Message</span>
        <span class="btn">Submit</span>
      </form>
    </div>
  </div>
</section>

<section class="services">
  <div class="wrap">
    <h2 class="section-title">OUR SERVICES</h2>
    <div class="service-row">
      <div class="service s1" role="img" aria-label="Runner stretching at sunset"></div>
      <div class="service s2" role="img" aria-label="Exercise ball session"></div>
      <div class="service s3" role="img" aria-label="Back stretch on a mat"></div>
    </div>
  </div>
</section>

<section class="contact">
  <div class="wrap">
    <h2 class="section-title">CONTACT</h2>
    <div class="locations">
      <div class="location">
        <div class="map" role="img" aria-label="Street map of the first practice location"></div>
        <h4>Contact Info</h4>
        <ul>
          <li><svg width="12" height="16" viewBox="0 0 12 16"><path fill="#6a3d9a" d="M6 0a6 6 0 0 0-6 6c0 4.5 6 10 6 10s6-5.5 6-10a6 6 0 0 0-6-6zm0 8.5a2.5 2.5 0 1 1 0-5 2.5 2.5 0 0 1 0 5z"/></svg>1234 Street Name, City Name, United States</li>
          <li><svg width="14" height="14" viewBox="0 0 24 24"><path fill="#6a3d9a" d="M6.6 10.8a15 15 0 0 0 6.6 6.6l2.2-2.2c.3-.3.7-.4 1-.2 1.1.4 2.3.6 3.6.6.6 0 1 .4 1 1V20c0 .6-.4 1-1 1A17 17 0 0 1 3 4c0-.6.4-1 1-1h3.5c.6 0 1 .4 1 1 0 1.3.2 2.5.6 3.6.1.3 0 .7-.2 1z"/></svg>(555) 123-5647</li>
          <li><svg width="14" height="11" viewBox="0 0 14 11"><rect width="14" height="11" fill="#6a3d9a"/><path d="m0 0 7 6 7-6" fill="none" stroke="#fff"/></svg><a href="#">Mail@example.com</a></li>
        </ul>
      </div>
      <div class="location">
        <div class="map" role="img" aria-label="Street map of the second practice location"></div>
        <h4>Contact Info</h4>
        <ul>
          <li><svg width="12" height="16" viewBox="0 0 12 16"><path fill="#6a3d9a" d="M6 0a6 6 0 0 0-6 6c0 4.5 6 10 6 10s6-5.5 6-10a6 6 0 0 0-6-6zm0 8.5a2.5 2.5 0 1 1 0-5 2.5 2.5 0 0 1 0 5z"/></svg>1234 Street Name, City Name, United States</li>
          <li><svg width="14" height="14" viewBox="0 0 24 24"><path fill="#6a3d9a" d="M6.6 10.8a15 15 0 0 0 6.6 6.6l2.2-2.2c.3-.3.7-.4 1-.2 1.1.4 2.3.6 3.6.6.6 0 1 .4 1 1V20c0 .6-.4 1-1 1A17 17 0 0 1 3 4c0-.6.4-1 1-1h3.5c.6 0 1 .4 1 1 0 1.3.2 2.5.6 3.6.1.3 0 .7-.2 1z"/></svg>(555) 123-5647</li>
          <li><svg width="14" height="11" viewBox="0 0 14 11"><rect width="14" height="11" fill="#6a3d9a"/><path d="m0 0 7 6 7-6" fill="none" stroke="#fff"/></svg><a href="#">Mail@example.com</a></li>
        </ul>
      </div>
    </div>
  </div>
</section>

<footer class="site-footer">
  <svg class="notch" width="44" height="22" viewBox="0 0 44 22"><path d="M0 0h44L22 22z" fill="#1bb3c9"/></svg>
  <div class="wrap">
    <div class="footer-cols">
      <div class="footer-col col-physio">
        <h4>Physiotherapy Services</h4>
        <ul>
          <li>Respiratory</li><li>Neurological rehabilitation</li><li>Oncology</li><li>Lymphoedema</li><li>Orthopaedics</li><li>Rheumatology</li>
          <li>Women's health</li><li>Paediatrics and neonates</li><li>Mental health</li><li>Learning disability (adults)</li><li>Hydrotherapy</li><li>Musculoskeletal</li>
        </ul>
      </div>
      <div class="footer-col col-psych">
        <h4>Psychology Services</h4>
        <ul><li>Lorem Ipsum</li><li>Lorem Ipsum</li><li>Lorem Ipsum</li><li>Lorem Ipsum</li><li>Lorem Ipsum</li><li>Lorem Ipsum</li></ul>
      </div>
      <div class="social-box">
        <strong>Brackenfold Health</strong>
        <div>242,597 people like Brackenfold Health.</div>
        <div class="faces"><span></span><span></span><span></span><span></span><span></span><span></span><span></span><span></span><span></span><span></span><span></span><span></span></div>
      </div>
    </div>
  </div>
  <div class="social"><b>Let's be Social</b><i></i><i></i><i></i><i></i><i></i></div>
  <div class="footer-bottom">
    <div class="wrap">
      <span>Copyright 2014 &copy; Brackenfold Health. All Rights Reserved.</span>
      <nav><span>Home</span><span>About</span><span>Contact</span><span>Terms &amp; Condition</span></nav>
    </div>
  </div>
</footer>

</body>
</html>
```